Business Card

Designs by L&M Renata Kowalczyk Signature Collection business card
Looking for a modern, classic and timeless business card for our jewelry company

Front of card should be a, all purple solid color for the background and white lettering like the attached document.

On the front of card:
Designs by L&M
Renata Kowalczyk Signature Collection
One of A Kind Designs for you!

Renata Fairbury
Owner

On the back on card
Email: LMDesigns27@postvela.com
Facepage: https://www.facepage-example.com/DesignsbyLMRenataandHolly
Chirpline:
https://chirpline-example.com/DesignsbyLM27
Picstream: http://picstream-example.com/DesignsbyLMjewelry

Industry/Entity Type

Business

```html
<!DOCTYPE html>
<html lang="en">
<head>
<meta charset="utf-8">
<title>Designs by L&amp;M — Business Card</title>
<link rel="stylesheet" href="https://fonts.googleapis.com/css2?family=Mulish:wght@300;400;700&display=swap">
<style>
  :root {
    --page: #efefef;
    --card-purple: #6f4a9e;
    --ink-light: #ffffff;
    --band-white: #ffffff;
    --band-grey: #b3b3b3;
  }
  * { box-sizing: border-box; margin: 0; padding: 0; }
  html, body {
    width: 1200px; height: 900px; overflow: hidden;
    background: var(--page);
    font-family: "Mulish", Arial, sans-serif;
    color: var(--ink-light);
  }
  .stage { position: relative; width: 1200px; height: 900px; }
  .card { position: absolute; background: var(--card-purple); }
  .card--back  { left: 373px; top: 420px; width: 705px; height: 410px; }
  .card--front { left: 93px;  top: 53px;  width: 712px; height: 412px; }

  /* Brand: plain name with one plain circle beside it */
  .brand { position: absolute; text-align: center; }
  .brand__name {
    display: inline-flex; align-items: center;
    font-weight: 400; white-space: nowrap;
  }
  .brand__dot {
    display: inline-block; border-radius: 50%;
    background: var(--ink-light);
  }
  .collection {
    display: block; font-weight: 300; white-space: nowrap;
  }

  .card--front .brand { left: 0; right: 0; top: 190px; }
  .card--front .brand__name { font-size: 28px; line-height: 34px; gap: 12px; }
  .card--front .brand__dot { width: 12px; height: 12px; }
  .card--front .collection { font-size: 15px; line-height: 20px; margin-top: 14px; }

  .card--back .brand { left: 430px; width: 220px; top: 278px; }
  .card--back .brand__name { font-size: 17px; line-height: 22px; gap: 8px; }
  .card--back .brand__dot { width: 8px; height: 8px; }
  .card--back .collection { font-size: 10px; line-height: 14px; margin-top: 6px; }

  .person { position: absolute; font-size: 16px; line-height: 21px; }
  .person__name { display: block; font-weight: 700; }
  .person__role { display: block; font-weight: 300; }
  .card--front .person { left: 58px; top: 328px; }
  .card--back  .person { left: 58px; top: 67px; }

  .tagline {
    position: absolute; right: 63px; top: 328px;
    font-size: 16px; line-height: 21px; font-weight: 300;
  }

  .contacts {
    position: absolute; left: 58px; top: 130px;
    border-collapse: collapse; font-size: 16px;
  }
  .contacts th {
    width: 95px; text-align: left; font-weight: 700;
    padding: 0; height: 29px;
    border-right: 1px solid var(--ink-light);
  }
  .contacts td { font-weight: 300; padding: 0 0 0 8px; }

  .pattern-band {
    position: absolute; left: 0; bottom: 0; width: 100%; height: 45px;
    background: linear-gradient(90deg, var(--band-white), var(--band-grey) 50%, var(--band-white));
  }
</style>
</head>
<body>
<main class="stage">

  <section class="card card--back" aria-label="Back of business card">
    <div class="person">
      <span class="person__name">Renata Fairbury</span>
      <span class="person__role">Owner</span>
    </div>
    <table class="contacts">
      <tr><th>Email</th><td>LMDesigns27@postvela.com</td></tr>
      <tr><th>Facepage</th><td>DesignsbyLMRenataandHolly</td></tr>
      <tr><th>Chirpline</th><td>DesignsbyLM27</td></tr>
      <tr><th>Picstream</th><td>DesignsbyLMjewelry</td></tr>
    </table>
    <div class="brand">
      <span class="brand__name"><span class="brand__dot"></span>Designs by L&amp;M</span>
      <span class="collection">Renata Kowalczyk Signature Collection</span>
    </div>
    <div class="pattern-band" role="img" aria-label="Band of alternating white, grey and purple-edged triangles"></div>
  </section>

  <section class="card card--front" aria-label="Front of business card">
    <div class="brand">
      <span class="brand__name"><span class="brand__dot"></span>Designs by L&amp;M</span>
      <span class="collection">Renata Kowalczyk Signature Collection</span>
    </div>
    <div class="person">
      <span class="person__name">Renata Fairbury</span>
      <span class="person__role">Owner</span>
    </div>
    <p class="tagline">One of A Kind Designs for you!</p>
  </section>

</main>
</body>
</html>
```